Institutional website for an IT Consulting company

Web design + HTML + CSS / Bootstrap + JS (interaction) integration in order to extend our existing website brightvale.coop.
Our website is currently aiming only for recruitment and not for customers, we want to provide a fluid transition between customer side website (this project) and recruitment website (existing site).

Ideally we would love the new design to be "inspired" by our actual graphic chart (Colors mainly). It should provide a great user experience and a landing page (or any mean) allowing the visitor to easily switch from the end customer front end (this project), the recruitment front end (existing front end https://www.brightvale.coop/) and the existing member front end (an other existing front end dedicated to members already existing).

In attachment you will find the expected site content mainly a one page with a first level of information and "link" to sub pages (a way to directly access this sub pages should also be provided).

The website should be accessible on mobile device and desktop.

The attachment is in french as it reflect the final site content, but if google translate isn't sufficient to have a general idea of the content, feel free to ask. We would love to have some visual representation for some categories.

Target Market(s)

fortune 500 companies

Industry/Entity Type

It Company

Coding

Coded - Design and coding required

Number of Pages Required

5+ page

Requirements
Must have
• This project must have an easy way to navigate between 3 sub sites, the customer one (the one designed here), the consultant / recruitment one (the existing one at brightvale.coop), the members one.

A one page experience at first leading to detail pages.

Custom made visuals to illustrate each categories.

Inspiration websites : quorb[.]fr ; tasknest[.]com ; dovrally[.] com ...

Be inspired by the existing color from our logo and existing website at brightvale[.]coop

```html
<!DOCTYPE html>
<html lang="en">
<head>
<meta charset="utf-8">
<title>brightvale.coop — Hire the best freelancers</title>
<link href="https://fonts.googleapis.com/css2?family=Montserrat:wght@300;400;500;600;700&display=swap" rel="stylesheet">
<style>
:root{
  --teal:#1aafb8;
  --teal-dark:#0b3f3f;
  --ink:#333333;
  --muted:#8a8a8a;
  --grey-soft:#f0f0f0;
  --grey-block:#bfbfbf;
  --white:#ffffff;
  --black:#000000;
}
*{box-sizing:border-box;margin:0;padding:0}
html,body{width:1200px;height:2829px;overflow:hidden}
body{position:relative;font-family:'Montserrat',sans-serif;color:var(--ink);background:var(--white)}
.abs{position:absolute}
a{color:inherit;text-decoration:none}

/* top bar */
.topbar{left:0;top:0;width:1200px;height:48px;background:var(--teal);color:var(--white);font-size:11px}
.topbar .contact{top:12px;display:flex;align-items:center;gap:10px}
.topbar .switch{left:747px;top:10px;height:28px;padding:0 12px;border:1px solid var(--white);border-radius:6px;font-size:12px;display:flex;align-items:center}
.topbar .member{left:985px;top:17px}

/* hero */
.hero{left:0;top:48px;width:1200px;height:728px;background:var(--black)}
.header{left:99px;top:48px;width:1003px;height:87px;background:var(--white);border-bottom:5px solid #d6d6d6}
.brand{font-weight:700;color:var(--teal-dark);font-size:24px;letter-spacing:.5px;display:flex;align-items:center;gap:8px}
.brand .dot{width:12px;height:12px;background:var(--teal)}
.header .brand{left:75px;top:28px}
.nav{right:35px;top:31px;display:flex;gap:30px;font-size:14px;color:var(--ink)}
.hero-title{left:0;top:280px;width:1200px;text-align:center;color:var(--white);font-weight:700;font-size:44px;line-height:52px}
.search{left:179px;top:423px;width:840px;height:62px;background:var(--white);border-radius:3px}
.search .field{top:0;height:62px;display:flex;align-items:center;gap:6px;color:#9a9a9a;font-size:13px}
.search .divider{left:444px;top:8px;width:1px;height:46px;background:#ddd}
.search .btn{right:5px;top:5px;width:97px;height:52px;background:var(--teal);color:var(--white);border-radius:3px;display:flex;align-items:center;justify-content:center;font-size:16px}

/* newsletter */
.newsletter{left:99px;top:664px;width:1003px;height:192px}
.newsletter p{position:absolute;left:30px;top:56px;width:570px;color:var(--white);font-weight:300;font-size:21px;line-height:26px}
.newsletter .email{left:622px;top:74px;width:231px;height:40px;border:2px solid var(--white);border-radius:6px;color:var(--white);font-size:12px;padding:12px 22px}
.newsletter .join{left:869px;top:76px;width:98px;height:36px;background:var(--white);border-radius:6px;color:var(--teal);font-weight:700;font-size:16px;display:flex;align-items:center;justify-content:center}

/* why us */
.why-title{left:0;top:905px;width:1200px;text-align:center;font-size:34px;font-weight:700;color:#666}
.why-lead{left:180px;top:965px;width:840px;text-align:center;font-size:21px;font-weight:300;line-height:31px;color:var(--muted)}
.feature{top:1086px;width:310px;text-align:center;font-size:13px;line-height:21px;color:var(--ink)}
.feature .icon{width:98px;height:98px;border-radius:50%;background:var(--teal);margin:0 auto 20px;display:flex;align-items:center;justify-content:center}
.vline{top:1094px;width:1px;height:182px;background:#ccc}

/* split block */
.split-text{left:99px;top:1370px;width:504px;height:326px;background:var(--grey-soft);padding:30px 38px}
.split-text h2{font-size:22px;font-weight:500;line-height:26px;margin-bottom:32px}
.split-text li{list-style:none;display:flex;gap:24px;font-size:13px;line-height:21px;margin-bottom:14px}
.split-text li svg{flex:0 0 38px}
.split-image{left:603px;top:1370px;width:499px;height:326px;background:var(--grey-block)}

/* testimonials */
.testimonials{left:0;top:1773px;width:1200px;height:542px;background:var(--teal);color:var(--white)}
.testimonials .kicker{position:absolute;top:46px;width:1200px;text-align:center;font-weight:700;font-size:17px}
.testimonials h2{position:absolute;top:72px;width:1200px;text-align:center;font-weight:700;font-size:35px}
.quote{top:175px;width:317px;height:218px;background:var(--teal-dark);padding:50px 30px;font-size:17px;line-height:21px}
.avatar{width:100px;height:100px;border-radius:50%;background:var(--white);border:7px solid #e3e3e3}
.person{font-size:13px;line-height:16px}
.person b{font-weight:700}

/* footer */
.footer .brand{left:99px;top:2393px}
.footer .about{left:99px;top:2457px;width:280px;font-size:13px;line-height:25.7px}
.social{top:2644px;width:43px;height:43px;border-radius:50%;background:var(--teal)}
.links{top:2383px;font-size:13px}
.links h3{font-size:17px;font-weight:600;margin-bottom:24px}
.links li{list-style:none;line-height:25.7px}
.copyright{left:0;top:2747px;width:1200px;height:82px;background:var(--grey-soft);text-align:center;font-size:11px;padding-top:38px}
</style>
</head>
<body>

<div class="abs topbar">
  <div class="abs contact" style="left:104px">
    <svg width="20" height="16" viewBox="0 0 20 16"><rect x="1" y="3" width="18" height="12" fill="#fff"/><path d="M1 3 L10 10 L19 3" stroke="#1aafb8" stroke-width="1.5" fill="none"/></svg>
    <span>xxxx@postmail.com</span>
  </div>
  <div class="abs contact" style="left:281px">
    <svg width="20" height="20" viewBox="0 0 20 20"><path d="M4 1 L8 5 L6 8 Q9 13 12 14 L15 12 L19 16 L16 19 Q8 19 1 5 Z" fill="#fff"/></svg>
    <span>01 23 45 67 89</span>
  </div>
  <a class="abs switch" href="https://www.brightvale.coop/">Je souhaite rejoindre Brightvale</a>
  <a class="abs member">Je suis Brightvale</a>
</div>

<div class="abs hero"></div>
<header class="abs header">
  <div class="abs brand"><span>brightvale.coop</span><span class="dot"></span></div>
  <nav class="abs nav"><a>Page 1</a><a>Page 2</a><a>Page 3</a><a>Page 4</a></nav>
</header>

<h1 class="abs hero-title">Hire the best freelancers<br>for any job</h1>

<div class="abs search">
  <div class="abs field" style="left:22px">
    <svg width="14" height="14" viewBox="0 0 14 14"><circle cx="5.5" cy="5.5" r="4.2" stroke="#999" stroke-width="2" fill="none"/><path d="M8.5 8.5 L13 13" stroke="#999" stroke-width="2"/></svg>
    <span>Try "React.js", "java", "UX designer" ...</span>
  </div>
  <div class="abs divider"></div>
  <div class="abs field" style="left:462px">
    <svg width="12" height="15" viewBox="0 0 12 15"><path d="M6 15 L1.5 8 A5 5 0 1 1 10.5 8 Z" fill="#999"/><circle cx="6" cy="5.5" r="2" fill="#fff"/></svg>
    <span>Country, Region, City ...</span>
  </div>
  <a class="abs btn">Search</a>
</div>

<section class="abs newsletter">
  <svg class="abs" style="left:0;top:0" width="1003" height="192" viewBox="0 0 1003 192">
    <path d="M6 0 L997 29 Q1003 29 1003 35 L1003 171 Q1003 177 997 177 L177 177 L168 192 L159 177 L6 177 Q0 177 0 171 L0 6 Q0 0 6 0 Z" fill="#1aafb8"/>
  </svg>
  <p>Lorem ipsum dolor sit amet, consectetur adipisicing elit, sed do eiusmod tempor incididunt ut labore et dolore magna aliqua.</p>
  <div class="abs email">enter email address</div>
  <a class="abs join">Join</a>
</section>

<h2 class="abs why-title">Why us?</h2>
<p class="abs why-lead">Vici nisi etiam orci faucibus felis justo sem cras viverra sociis rutrum neque. Massa sit sociis sapien. Rhoncus eu adipiscing integer laoreet a ante metus vidi massa. Aenean eleifend.</p>

<div class="abs feature" style="left:102px">
  <div class="icon"><svg width="54" height="54" viewBox="0 0 54 54"><circle cx="40" cy="12" r="7" fill="#fff"/><circle cx="13" cy="27" r="7" fill="#fff"/><circle cx="40" cy="42" r="7" fill="#fff"/><path d="M13 27 L40 12 M13 27 L40 42" stroke="#fff" stroke-width="4"/></svg></div>
  Vici nisi etiam orci faucibus felis justo sem cras viverra sociis rutrum neque. Massa sit sociis sapien. Rhoncus eu adipiscing integer laoreet a ante metus vidi massa. Aenean eleifend.
</div>
<div class="abs vline" style="left:428px"></div>
<div class="abs feature" style="left:445px">
  <div class="icon"><svg width="50" height="62" viewBox="0 0 50 62"><path d="M25 4 A19 19 0 0 0 13 38 L16 48 L34 48 L37 38 A19 19 0 0 0 25 4 Z" stroke="#fff" stroke-width="5" fill="none"/><path d="M19 55 L31 55" stroke="#fff" stroke-width="5"/></svg></div>
  Vici nisi etiam orci faucibus felis justo sem cras viverra sociis rutrum neque. Massa sit sociis sapien. Rhoncus eu adipiscing integer laoreet a ante metus vidi massa. Aenean eleifend.
</div>
<div class="abs vline" style="left:772px"></div>
<div class="abs feature" style="left:789px">
  <div class="icon"><svg width="58" height="58" viewBox="0 0 58 58"><circle cx="29" cy="29" r="25" stroke="#fff" stroke-width="6" fill="none"/><path d="M29 14 L29 30 L42 30" stroke="#fff" stroke-width="5" fill="none"/></svg></div>
  Vici nisi etiam orci faucibus felis justo sem cras viverra sociis rutrum neque. Massa sit sociis sapien. Rhoncus eu adipiscing integer laoreet a ante metus vidi massa. Aenean eleifend.
</div>

<section class="abs split-text">
  <h2>Lorem ipsum dolor siamet conse ctetur adipi sicing elit sed doni.</h2>
  <ul>
    <li><svg width="38" height="36" viewBox="0 0 38 36"><path d="M3 20 L13 31 L35 3" stroke="#888" stroke-width="6" fill="none"/></svg><span>Vici nisi etiam orci faucibus felis justo sem cras viverra sociis rutrum neque.</span></li>
    <li><svg width="38" height="36" viewBox="0 0 38 36"><path d="M3 20 L13 31 L35 3" stroke="#888" stroke-width="6" fill="none"/></svg><span>Vici nisi etiam orci faucibus felis justo sem cras viverra sociis rutrum neque.</span></li>
    <li><svg width="38" height="36" viewBox="0 0 38 36"><path d="M3 20 L13 31 L35 3" stroke="#888" stroke-width="6" fill="none"/></svg><span>Vici nisi etiam orci faucibus felis justo sem cras viverra sociis rutrum neque.</span></li>
  </ul>
</section>
<div class="abs split-image" role="img" aria-label="Image placeholder illustrating the service"></div>

<section class="abs testimonials">
  <div class="kicker">Testimonials</div>
  <h2>What Our Clients Say</h2>

  <div class="abs quote" style="left:99px">”Credibly innovate granular internal or "organic" sources whereas high standards in web readiness.</div>
  <div class="abs avatar" role="img" aria-label="Client portrait" style="left:116px;top:363px"></div>
  <div class="abs person" style="left:231px;top:408px"><b>MARCO DELVANI</b><br>Ceo</div>

  <div class="abs quote" style="left:442px;padding-top:43px">”Credibly innovate granular internal or "organic" sources whereas high standards in web readiness.</div>
  <div class="abs avatar" role="img" aria-label="Client portrait" style="left:458px;top:363px"></div>
  <div class="abs person" style="left:583px;top:408px"><b>MARCO DELVANI</b><br>Ceo</div>

  <div class="abs quote" style="left:785px;padding-top:37px">”Credibly innovate granular internal or "organic" sources whereas high standards in web readiness.</div>
  <div class="abs avatar" role="img" aria-label="Client portrait" style="left:802px;top:363px"></div>
  <div class="abs person" style="left:926px;top:408px"><b>MARCO DELVANI</b><br>Ceo</div>
</section>

<footer class="footer">
  <div class="abs brand"><span>brightvale.coop</span><span class="dot"></span></div>
  <p class="abs about">Vero eos et accusamus et iusto odio dignissimos ducimus qui blanditiis praesentium voluptatum deleniti atque corrupti quos dolores et quasoa molestias excepturi sintal occaecati cupiditate non provident similique sunt.</p>
  <a class="abs social" style="left:99px" aria-label="Social profile"></a>
  <a class="abs social" style="left:159px" aria-label="Social profile"></a>
  <a class="abs social" style="left:219px" aria-label="Social profile"></a>
  <a class="abs social" style="left:279px" aria-label="Social profile"></a>

  <div class="abs links" style="left:500px"><h3>Quick Links</h3><ul><li>Home</li><li>About</li><li>Company</li><li>Our Services</li><li>Service</li><li>Location</li><li>Recent News</li><li>Contact us</li></ul></div>
  <div class="abs links" style="left:722px"><h3>Quick Links</h3><ul><li>Home</li><li>About</li><li>Company</li><li>Our Services</li><li>Service</li><li>Location</li><li>Recent News</li><li>Contact us</li></ul></div>
  <div class="abs links" style="left:954px"><h3>Quick Links</h3><ul><li>Home</li><li>About</li><li>Company</li><li>Our Services</li><li>Service</li><li>Location</li><li>Recent News</li><li>Contact us</li></ul></div>

  <div class="abs copyright">© 2015, All Rights Reserved.</div>
</footer>

</body>
</html>
```